Qolvar Energy Information Site Redesign

Re-vamp current site at qolvarenergy.com to include new logo, verbiage updates as needed, redesign, etc. Company overview and additional information on current QVR url.

```html
<!DOCTYPE html>
<html lang="en">
<head>
<meta charset="utf-8">
<title>Qolvar Energy Information</title>
<link href="https://fonts.googleapis.com/css2?family=Raleway:wght@300;400;600;700&display=swap" rel="stylesheet">
<style>
  :root {
    --header-bg: #eceef0;
    --brand-blue: #2b6fb6;
    --nav-blue: #2f7cc0;
    --nav-text: #ffffff;
    --hero-deep: #22426a;
    --hero-mid: #3d6690;
    --hero-light: #7f93a8;
    --hero-text: #ffffff;
    --dot-active: #e58a2a;
    --dot-idle: #f4f4f4;
  }
  * { margin: 0; padding: 0; box-sizing: border-box; }
  html, body {
    width: 1200px;
    height: 800px;
    overflow: hidden;
    font-family: "Raleway", Arial, sans-serif;
    background: var(--header-bg);
  }
  .site {
    width: 1200px;
    height: 800px;
    display: flex;
    flex-direction: column;
  }
  .site-header {
    height: 150px;
    background: var(--header-bg);
    display: flex;
    align-items: center;
    justify-content: center;
  }
  .brand {
    display: flex;
    align-items: center;
    gap: 12px;
    color: var(--brand-blue);
    font-weight: 600;
    font-size: 26px;
    letter-spacing: 0.5px;
    text-decoration: none;
  }
  .brand-mark {
    width: 22px;
    height: 22px;
    border-radius: 50%;
    background: var(--brand-blue);
  }
  .main-nav {
    height: 86px;
    background: var(--nav-blue);
    display: flex;
    align-items: center;
    justify-content: center;
  }
  .main-nav ul {
    list-style: none;
    display: flex;
    gap: 27px;
    transform: translateX(5px);
  }
  .main-nav a {
    color: var(--nav-text);
    text-decoration: none;
    font-weight: 600;
    font-size: 15.5px;
    display: flex;
    align-items: center;
    gap: 5px;
  }
  .caret { width: 9px; height: 6px; fill: var(--nav-text); }
  .hero {
    position: relative;
    flex: 1;
    overflow: hidden;
  }
  .hero-photo {
    position: absolute;
    inset: 0;
    background:
      radial-gradient(ellipse at 12% 30%, rgba(150,150,150,0.55), transparent 45%),
      radial-gradient(ellipse at 10% 90%, rgba(200,200,205,0.5), transparent 30%),
      linear-gradient(180deg, var(--hero-mid) 0%, var(--hero-deep) 70%, #1f3d63 100%);
  }
  .hero-tint {
    position: absolute;
    inset: 0;
    background: rgba(30, 60, 100, 0.25);
  }
  .hero-statement {
    position: absolute;
    top: 162px;
    left: 0;
    right: 0;
    text-align: center;
    color: var(--hero-text);
    font-weight: 400;
    font-size: 33px;
    line-height: 48px;
    text-shadow: 0 1px 3px rgba(0,0,0,0.35);
  }
  .slider-dots {
    position: absolute;
    bottom: 33px;
    left: 0;
    right: 0;
    display: flex;
    justify-content: center;
    gap: 15px;
  }
  .slider-dot {
    width: 19px;
    height: 19px;
    border-radius: 50%;
    background: var(--dot-idle);
  }
  .slider-dot.is-active { background: var(--dot-active); }
</style>
</head>
<body>
<div class="site">
  <header class="site-header">
    <a class="brand" href="#">
      <span class="brand-mark"></span>
      <span class="brand-name">Qolvar Energy Information</span>
    </a>
  </header>

  <nav class="main-nav">
    <ul>
      <li><a href="#">What We Do</a></li>
      <li><a href="#">Exchange Solutions <svg class="caret" viewBox="0 0 10 6"><path d="M0 0h10L5 6z"/></svg></a></li>
      <li><a href="#">Data Management <svg class="caret" viewBox="0 0 10 6"><path d="M0 0h10L5 6z"/></svg></a></li>
      <li><a href="#">Owner Relations Services</a></li>
      <li><a href="#">About QVR <svg class="caret" viewBox="0 0 10 6"><path d="M0 0h10L5 6z"/></svg></a></li>
      <li><a href="#">Blog</a></li>
    </ul>
  </nav>

  <section class="hero">
    <div class="hero-photo" role="img" aria-label="Collage of an oil pumpjack, storage tanks, an offshore drilling platform and a blue gas flame"></div>
    <div class="hero-tint"></div>
    <p class="hero-statement">
      Our services allow companies to enhance productivity<br>
      by accelerating information flow, reducing costs<br>
      and delivering consistent, timely and complete<br>
      information to their business partners.
    </p>
    <div class="slider-dots">
      <span class="slider-dot is-active"></span>
      <span class="slider-dot"></span>
    </div>
  </section>
</div>
</body>
</html>
```